Velvetorchid Hair & Beauty Business Card

Velvetorchid Hair & Beauty is a boutique salon located in the picturesque Lake Taupo NZ. The salon is very luxurious, opulent gold gilded mirrors, chandelier lit, contemporary french decor, sets the mood to create beautiful hair, makeup and all beauty services. Just had a new logo design and now after a new business card.
Logo
14 Korowhai Street
Taupo
Phone (07) 548 6193
www.velvetorchid.co.nz
email hair@velvetorchid.co.nz
Marlena Swithin
Also need a space to put in Stylist name, date, appointment time. thanks;)
Another idea is we could incorporate the wallpaper in the back ground either on the back or front or use an ornate glided frame (around the edge of the card) like on my website where my brides photos flash.
Decided against the wall paper but at least you can see our colour theme for the salon.
Updates

Please check out my updated brief . Thanks :)

Target Market(s)

25-60 years plus, mainly mid age females , wanting the best possible service , high standard of workmanship and money not a problem.

Industry/Entity Type

Boutique

Requirements
Must have
• Gold and silver

```html
<!DOCTYPE html>
<html lang="en">
<head>
<meta charset="utf-8">
<title>Velvetorchid Hair &amp; Beauty – Business Card</title>
<link rel="stylesheet" href="https://fonts.googleapis.com/css2?family=Questrial&display=swap">
<style>
  :root {
    --card-gold: #b39700;
    --field-silver: #8fa3a0;
    --ink: #2b0d08;
  }
  html, body {
    margin: 0;
    padding: 0;
    width: 1200px;
    height: 702px;
    overflow: hidden;
    background: var(--card-gold);
  }
  .card {
    position: relative;
    width: 1200px;
    height: 702px;
    background: var(--card-gold);
    font-family: "Questrial", "Century Gothic", sans-serif;
    color: var(--ink);
    text-transform: uppercase;
  }
  .appointment-field {
    position: absolute;
    top: 93px;
    width: 270px;
  }
  .appointment-field .field-box {
    display: block;
    width: 270px;
    height: 43px;
    background: var(--field-silver);
  }
  .appointment-field .field-label {
    position: absolute;
    top: 49px;
    left: -40px;
    right: -40px;
    text-align: center;
    font-size: 23px;
    line-height: 1;
    letter-spacing: 0.01em;
  }
  .field-stylist { left: 71px; }
  .field-date { left: 467px; }
  .field-time { left: 858px; }
  .field-stylist .field-label { left: -40px; right: -20px; text-align: center; }
  .field-time .field-label { left: -10px; right: -10px; }

  .contact-block {
    position: absolute;
    top: 204px;
    left: 0;
    width: 1200px;
    margin: 0;
    padding: 0;
    list-style: none;
    text-align: center;
  }
  .contact-block li {
    font-size: 47px;
    line-height: 61px;
    height: 61px;
    letter-spacing: 0.03em;
    white-space: nowrap;
  }
</style>
</head>
<body>
  <main class="card">
    <div class="appointment-field field-stylist">
      <span class="field-box"></span>
      <span class="field-label">Stylist Name</span>
    </div>
    <div class="appointment-field field-date">
      <span class="field-box"></span>
      <span class="field-label">Date</span>
    </div>
    <div class="appointment-field field-time">
      <span class="field-box"></span>
      <span class="field-label">Appointment Time</span>
    </div>

    <ul class="contact-block">
      <li class="salon-name">Velvetorchid Hair &amp; Beauty</li>
      <li class="street">14 Korowhai Street</li>
      <li class="town">Taupo</li>
      <li class="phone">Phone (07) 548 6193</li>
      <li class="website">www.velvetorchid.co.nz</li>
      <li class="email">Email hair@velvetorchid.co.nz</li>
      <li class="owner">Marlena Swithin</li>
    </ul>
  </main>
</body>
</html>
```